Urkundendesign für Jahrgangsbeste einer Realschule gesucht
Der Elternbeirat der Realschule Lindwerth benötigt für die Jahrgangsbesten des Abschlussjahrgangs eine Urkunde. Gerne mit Prägung (was kostet sowas bei Druck?!?). Das von-Halmberg-Logo darf benutzt werden (siehe Homepage).
es soll eine Urkunde für den/die 'Jahrgangsbeste 2026' geben. das Datum, sowie SchülerInnen-Name würden wir jeweils handschriftlich anbringen.
die Urkunde in A4 gestalten.
wir benötigen die üblichen druckbaren Dateien, sodass eine Druckerei dann auch selbst Jahr für Jahr das Jahr abändern kann.
bitte um Vorschläge, wir arbeiten uns nach und nach da durch.
nicht zu viel Schnörkelei.

```html
<!DOCTYPE html>
<html lang="de">
<head>
<meta charset="utf-8">
<title>Urkunde – Variante 1</title>
<link href="https://fonts.googleapis.com/css2?family=Jost:wght@300;500;600&family=Inter:wght@400&family=Caveat:wght@400&display=swap" rel="stylesheet">
<style>
  :root{
    --teal:#27b09e;
    --green:#56a82c;
    --lime:#9bc31c;
    --ink:#2e2e2e;
    --label:#a9a9a9;
    --rule:#8fcf6a;
    --paper:#ffffff;
    --page:#ffffff;
    --photo-light:#f1efed;
    --photo-mid:#dccbb8;
    --photo-dark:#7d634c;
  }
  *{margin:0;padding:0;box-sizing:border-box}
  html,body{width:1200px;height:2553px;overflow:hidden;background:var(--page)}
  body{position:relative;font-family:"Inter",Arial,sans-serif;color:var(--ink)}
  .variant-label{
    position:absolute;top:71px;left:0;width:1200px;text-align:center;
    font-family:"Jost",Arial,sans-serif;font-weight:300;font-size:20px;
    letter-spacing:4.6px;color:var(--label);
  }
  .certificate{
    position:absolute;left:273px;top:228px;width:654px;height:925px;
    background:var(--paper);
    box-shadow:6px 10px 22px rgba(0,0,0,.22);
  }
  .band{position:absolute;left:0;width:100%;height:18px;
    background:linear-gradient(90deg,var(--lime),var(--teal))}
  .band--top{top:0}
  .band--bottom{bottom:0}
  .school-mark{
    position:absolute;top:85px;left:0;width:100%;
    display:flex;justify-content:center;align-items:center;gap:9px;
    font-family:"Jost",Arial,sans-serif;font-weight:600;font-size:17px;color:var(--green);
  }
  .school-mark__dot{width:14px;height:14px;border-radius:50%;background:var(--teal)}
  .title{
    position:absolute;top:160px;left:0;width:100%;text-align:center;
    font-family:"Jost",Arial,sans-serif;font-weight:500;font-size:92px;line-height:1;
    letter-spacing:7px;color:var(--teal);padding-left:7px;
  }
  .subtitle{
    position:absolute;top:272px;left:0;width:100%;text-align:center;
    font-family:"Jost",Arial,sans-serif;font-weight:600;font-size:31px;line-height:1;
    letter-spacing:2.4px;color:var(--green);
  }
  .text{
    position:absolute;left:0;width:100%;text-align:center;
    font-size:12.4px;line-height:20px;color:var(--ink);
  }
  .text--intro{top:353px}
  .text--praise{top:570px}
  .text--wishes{top:673px}
  .field{position:absolute;border-bottom:1px solid var(--rule);text-align:center;
    font-family:"Caveat",cursive;color:var(--ink)}
  .field--name{left:112px;width:429px;top:462px;height:61px;font-size:40px;line-height:58px}
  .field--date{left:112px;width:177px;top:800px;height:35px;font-size:24px;line-height:36px}
  .field--sign{left:318px;width:223px;top:800px;height:35px;font-size:24px;line-height:36px}
  .field-caption{position:absolute;font-size:8px;color:var(--ink)}
  .field-caption--date{left:112px;top:841px}
  .field-caption--sign{right:112px;top:845px}
  .mockup-photo{
    position:absolute;left:0;top:1353px;width:1200px;height:1200px;
    background:
      linear-gradient(160deg,var(--photo-light) 0%,var(--photo-light) 35%,var(--photo-mid) 65%,var(--photo-dark) 100%);
  }
</style>
</head>
<body>
  <div class="variant-label">URKUNDE – VARIANTE 1</div>

  <article class="certificate">
    <div class="band band--top"></div>

    <div class="school-mark"><span class="school-mark__dot"></span>Realschule Lindwerth</div>

    <h1 class="title">URKUNDE</h1>
    <h2 class="subtitle">JAHRGANGSBESTE/R 2026</h2>

    <p class="text text--intro">Die Karl-Anton-von-Halmberg-Realschule<br>in Lindwerth verleiht diese Urkunde in Anerkennung<br>herausragender schulischer Leistungen an:</p>

    <div class="field field--name">Vorname Nachname</div>

    <p class="text text--praise">Mit außergewöhnlichem Engagement, Ausdauer und Zielstrebigkeit<br>wurde während der gesamten Schulzeit eine Leistung erbracht, die<br>besondere Anerkennung und höchste Wertschätzung verdient.</p>

    <p class="text text--wishes">Zu diesem herausragenden Erfolg gratulieren wir herzlich und wünschen<br>für den weiteren Lebensweg alles Gute und viel Erfolg.</p>

    <div class="field field--date">Ort, Datum</div>
    <div class="field field--sign">Unterschrift und Stempel</div>
    <span class="field-caption field-caption--date">Ort und Datum</span>
    <span class="field-caption field-caption--sign">Unterschrift</span>

    <div class="band band--bottom"></div>
  </article>

  <div class="mockup-photo" role="img" aria-label="Foto: Eine Person in weißem Shirt hält die gedruckte Urkunde vor einem hellen Hintergrund mit Holztisch"></div>
</body>
</html>
```